Moving comapny Postcard mailer Design

I am looking for a 6x9 postcard with real images of our team. I would like to add the same review we currently have , I want the colors of the postcard to be orange and white. I want the team picture to be enlarged with the other pictures to be mimized. I will add example postcards to give rough ideas. My company is called Harlow Moving and the postcards with that name are our current postcards. The additional postcards are from other companies who have better postcards than mine. My goal is for my postcard to be better that theirs.

Target Market(s)

Wealthy people in the 35+ age group

Industry/Entity Type

Moving company

Requirements
Must have
• Beauty

```html
<!DOCTYPE html>
<html lang="en">
<head>
<meta charset="utf-8">
<title>Harlow Moving Postcard</title>
<link rel="stylesheet" href="https://fonts.googleapis.com/css2?family=Alfa+Slab+One&family=Kaushan+Script&family=Montserrat:wght@500;600;700;800&display=swap">
<style>
:root{
  --stage:#2b2b2b;
  --orange:#f26a21;
  --orange-light:#f89a4c;
  --navy:#0f2e6e;
  --blue:#1f4fa0;
  --sky:#d3e4f5;
  --white:#ffffff;
  --ink:#1d2a44;
}
*{box-sizing:border-box;margin:0;padding:0}
html,body{width:1200px;height:1200px;overflow:hidden;background:var(--stage)}
body{position:relative;font-family:"Montserrat",Arial,sans-serif;color:var(--ink)}
.card{position:absolute;left:206px;width:790px;height:523px;background:var(--white);overflow:hidden}
.card--front{top:56px}
.card--back{top:611px;height:527px}
.layer{position:absolute;inset:0;width:100%;height:100%}
.abs{position:absolute}

/* front */
.eyebrow{left:13px;top:12px;font-family:"Alfa Slab One",serif;font-size:24px;line-height:30px;color:var(--orange);white-space:nowrap}
.eyebrow .script{font-family:"Kaushan Script",cursive;font-size:19px;margin-left:4px}
.brand-title{left:13px;top:50px;font-family:"Alfa Slab One",serif;font-weight:400;font-size:50px;line-height:47px;color:var(--navy)}
.phone-pill{left:4px;top:162px;width:262px;height:44px;border-radius:22px;background:var(--orange);border:3px solid var(--white);box-shadow:0 0 0 2px var(--orange);color:var(--white);font-family:"Alfa Slab One",serif;font-size:24px;display:flex;align-items:center;justify-content:center}
.team-photo{left:200px;top:62px;width:350px;height:325px}
.brand-mark{left:25px;top:330px;width:210px;display:flex;align-items:center;justify-content:center;gap:8px}
.brand-mark .square{width:18px;height:18px;background:var(--navy)}
.brand-mark .name{font-weight:800;font-size:21px;color:var(--navy);white-space:nowrap}
.dot-number{left:30px;top:466px;width:240px;text-align:center;font-size:14px;font-weight:600;color:#222}
.web{left:22px;top:494px;width:240px;text-align:center;font-size:15px;font-weight:800;color:#111;white-space:nowrap}
.web b{color:var(--blue)}
.stars{left:287px;top:388px;width:253px;height:43px;border-radius:22px;background:var(--blue);border:3px solid var(--sky);display:flex;align-items:center;justify-content:center}
.review{left:284px;top:447px;width:448px;font-size:11px;line-height:13.6px;color:#1b1b1b;text-align:center}
.review strong{color:var(--navy)}
.coupon{left:660px;width:130px;background:var(--navy);border:4px solid var(--orange-light);border-right:none;border-radius:10px 0 0 10px;color:var(--white);text-align:center;padding-top:10px}
.coupon .amt{font-weight:800;font-size:23px;line-height:24px}
.coupon .amt sup{font-size:13px;vertical-align:top}
.coupon .cond{font-size:13px;line-height:14px;font-weight:500;margin-top:3px}
.coupon .tag{margin:8px auto 0;width:92px;background:var(--orange);font-size:11px;line-height:16px;font-weight:500}
.c1{top:20px;height:114px}
.c2{top:155px;height:114px}
.c3{top:289px;height:117px}

/* back */
.headline{left:18px;top:12px;font-family:"Alfa Slab One",serif;font-weight:400;font-size:40px;line-height:42px;color:var(--orange);text-shadow:2px 3px 0 #bfbfbf;white-space:nowrap}
.intro{left:21px;top:106px;width:300px;font-size:11px;line-height:13.3px;color:#1b1b1b}
.hero-photo{left:322px;top:0;width:280px;height:208px}
.services-tab{left:0;top:217px;width:122px;height:23px;color:var(--white);font-weight:700;font-size:14px;line-height:23px;padding-left:16px}
.services{left:134px;top:222px;list-style:none;font-family:"Alfa Slab One",serif;font-size:16.5px;line-height:19.5px;color:var(--navy);white-space:nowrap}
.services li{position:relative;padding-left:14px}
.services li::before{content:"";position:absolute;left:0;top:5px;border-left:8px solid var(--orange);border-top:5px solid transparent;border-bottom:5px solid transparent}
.back-mark{left:20px;top:392px;width:220px;display:flex;align-items:center;justify-content:center;gap:8px}
.back-mark .square{width:16px;height:16px;background:var(--white)}
.back-mark .name{font-weight:800;font-size:19px;color:var(--white);white-space:nowrap}
.call-pill{left:12px;top:454px;width:213px;height:31px;border-radius:16px;background:var(--orange);border:2px solid var(--white);color:var(--white);font-family:"Alfa Slab One",serif;font-size:15px;display:flex;align-items:center;justify-content:center}
.back-phone{left:18px;top:494px;width:205px;text-align:center;color:var(--white);font-weight:800;font-size:20px}
</style>
</head>
<body>

<section class="card card--front">
  <div class="abs team-photo" role="img" aria-label="Photo of the moving crew standing in front of an open truck" style="background:linear-gradient(90deg,rgba(233,237,242,0),#b9c4c6 35%,#6f7f6c)"></div>

  <svg class="layer" viewBox="0 0 790 523" aria-hidden="true">
    <path d="M0 470 Q300 420 790 470 L790 523 L0 523 Z" fill="var(--sky)"/>
    <path d="M0 482 Q300 436 790 482 L790 523 L0 523 Z" fill="var(--white)"/>
    <polygon points="541,0 790,0 790,430 560,430 645,206" fill="var(--orange)"/>
    <polyline points="526,0 630,206 545,430" fill="none" stroke="var(--white)" stroke-width="9"/>
    <polyline points="512,0 615,206 530,430" fill="none" stroke="var(--orange)" stroke-width="4"/>
  </svg>

  <div class="abs eyebrow">ARE YOU MOVING?<span class="script">Let Us Handle Everything!</span></div>
  <h1 class="abs brand-title">HARLOW<br>MOVING</h1>
  <div class="abs phone-pill">(865) 555-0142</div>

  <div class="abs brand-mark"><span class="square"></span><span class="name">Harlow Moving</span></div>
  <div class="abs dot-number">DOT #4820117</div>
  <div class="abs web">WWW.<b>HARLOWMOVERS</b>.COM</div>

  <div class="abs stars" aria-label="Five star review">
    <svg width="200" height="30" viewBox="0 0 200 30" aria-hidden="true">
      <g fill="var(--white)">
        <polygon points="20,2 24,11 34,11 26,17 29,27 20,21 11,27 14,17 6,11 16,11"/>
        <polygon points="60,2 64,11 74,11 66,17 69,27 60,21 51,27 54,17 46,11 56,11"/>
        <polygon points="100,2 104,11 114,11 106,17 109,27 100,21 91,27 94,17 86,11 96,11"/>
        <polygon points="140,2 144,11 154,11 146,17 149,27 140,21 131,27 134,17 126,11 136,11"/>
        <polygon points="180,2 184,11 194,11 186,17 189,27 180,21 171,27 174,17 166,11 176,11"/>
      </g>
    </svg>
  </div>
  <p class="abs review"><strong>The company is incredible!</strong> After working all day, they came to our house and without skipping a beat began efficiently moving our heavy household items. They had a great attitude, very friendly, and clearly enjoyed working with each other! They took extremely good care of my household items. <strong>Thank you for a great experience!</strong></p>

  <div class="abs coupon c1"><div class="amt"><sup>$</sup>25 OFF</div><div class="cond">MOVES<br>UNDER 1000</div><div class="tag">With this card</div></div>
  <div class="abs coupon c2"><div class="amt"><sup>$</sup>50 OFF</div><div class="cond">MOVES<br>OVER 1000</div><div class="tag">With this card</div></div>
  <div class="abs coupon c3"><div class="amt"><sup>$</sup>100 OFF</div><div class="cond">MOVES<br>OVER 3000</div><div class="tag">With this card</div></div>
</section>

<section class="card card--back">
  <div class="abs hero-photo" role="img" aria-label="Photo of two movers carrying boxes from a truck" style="background:linear-gradient(100deg,rgba(240,243,247,0),#dfe9f3 18%,#9fb3c8 55%,#39507a)"></div>

  <svg class="layer" viewBox="0 0 790 527" aria-hidden="true">
    <polygon points="0,362 270,338 250,527 0,527" fill="var(--navy)"/>
    <polygon points="0,350 272,326 270,336 0,360" fill="var(--blue)"/>
    <rect x="0" y="208" width="600" height="5" fill="var(--orange)"/>
    <polygon points="0,217 112,217 122,228 112,240 0,240" fill="var(--orange)"/>
    <polygon points="575,0 598,0 648,110 598,208 575,208 625,110" fill="var(--orange)"/>
    <polygon points="381,226 584,226 561,306 358,306" fill="#c6ccd2"/>
    <polygon points="584,226 597,226 574,306 561,306" fill="var(--orange)"/>
    <polygon points="346,318 529,318 508,392 325,392" fill="#c7cdc8"/>
    <polygon points="529,318 542,318 521,392 508,392" fill="var(--orange)"/>
    <polygon points="320,410 480,410 456,490 296,490" fill="#aeb8b3"/>
    <polygon points="480,410 493,410 469,490 456,490" fill="var(--navy)"/>
  </svg>

  <div class="abs" role="img" aria-label="Photo of a moving truck and ramp outside a home" style="left:358px;top:226px;width:226px;height:80px;clip-path:polygon(23px 0,100% 0,calc(100% - 23px) 100%,0 100%);background:linear-gradient(135deg,#d9dde0,#a8b1b7)"></div>
  <div class="abs" role="img" aria-label="Photo of movers wrapping furniture on a driveway" style="left:325px;top:318px;width:204px;height:74px;clip-path:polygon(21px 0,100% 0,calc(100% - 21px) 100%,0 100%);background:linear-gradient(135deg,#dfe3e0,#aab4ac)"></div>
  <div class="abs" role="img" aria-label="Photo of movers carrying a sofa into a house" style="left:296px;top:410px;width:184px;height:80px;clip-path:polygon(24px 0,100% 0,calc(100% - 24px) 100%,0 100%);background:linear-gradient(135deg,#c9d0cc,#8e9a93)"></div>
  <div class="abs" role="img" aria-label="Photo of a white box truck" style="left:462px;top:400px;width:178px;height:118px;background:linear-gradient(180deg,#f4f5f7,#d7dbe0)"></div>

  <h2 class="abs headline">MOVING<br>MADE SIMPLE!</h2>
  <p class="abs intro">For over 10 years, our team at Harlow Moving has been providing Eastern Tennessee with unparalleled custom moving experiences. We prioritize safety, timeliness, and communication to ensure our customers are happy and stress-free before, during, and after their move. No matter where you need to go, we're here to help!</p>

  <div class="abs services-tab">SERVICES</div>
  <ul class="abs services">
    <li>Local Moving</li>
    <li>Interstate Moving</li>
    <li>Packing &amp; Unpacking</li>
    <li>Hourly Labor</li>
    <li>Junk Removal</li>
  </ul>

  <div class="abs back-mark"><span class="square"></span><span class="name">Harlow Moving</span></div>
  <div class="abs call-pill">CALL US TODAY</div>
  <div class="abs back-phone">(865) 555-0142</div>
</section>

</body>
</html>
```